Store Front Window Design

We have a beautiful corner store front dental practice with no window signage. Crazy I know...that's why we need your help.

The final design will be done in all vinyl unless unless you suggest a different medium (meaning we are open to some design idea like using frosted glass, etc...).

The windows provide a lot of natural light so the design needs to keep a lot of natural light coming into the office. Keep in mind vinyl is not opaque so keep the signage aesthetically pleasing and a minimalist design to allow as much natural light in as possible. The design should follow the aesthetic from our logo. or tie into at least. We want a cohesive brand aesthetic.

I submitted some general layout ideas. There is a blue banner with advertising words which we want to be used in the final version. Even though the lettering is black, in reality the letters will be a white vinyl on the outside of the window. When you submit your work, be sure to add any special instructions (aka tell me the vision for the letters is white not black, maybe gold leaf, or forested glass...stuff like that). AND YOU DO NOT HAVE TO FOLLOW MY PATTERN! YOU ARE ARTISTS AND WE ARE LOOKING FOR AN ARTISTIC EYE CATCHING PRESENTATION OF THIS INFORMATION. MAKE IT FLASHY AND ADD SOME AESTHETIC FROM THE TOOTH LOGO.

The store front is 6 windows roughly 60'' x 36'' The smaller windows below are 27'' x 36''. Around the corner there are 3 windows. they are 60'' x 27'' lower windows are 27" x 27". We would like to keep the bottom windows clear and keep the signage on the top windows, however, we are flexible.

The front 6 windows need to have this information worked into the design.

Practice name: Venn and Obradovic Dental & Orthodontics.
Phone numbers: Maren Venn DDS: 555.218.7043
Piotr Obradovic DDS:555.731.0962

Expertise: Dr. Venn General Dentistry & Orthodontics
Dr. Obradovic Oral Surgery & Sedation

Address: 4819 Thistle Rd

A banner across the bottom of the top windows with some key advertisement words: "Clearvetta" "Braces" "Implants" "Whiting" "Call today" "Free Consultation" "Oral Surgery" "Sedation". We like the two color idea. Its up to you to decide on the color combo. I used a Dark and light blue, but maybe a Blue and grey would nice to tire in the logo colors?

I have made some mock ideas to get the ball rolling but you do not have to stick to these designs at all, just as long as all the required information is there. Be creative with the layouts, fonts, color scheme, (just remember these are going on windows not necessarily a white background), and graphics/artistic flare (refer to logo for layout inspiration and use the logo as an actual graphic). We are running a miltimillion dollar dental practice so we want these windows to be eye catching to pull in patients and look like a million dollar design. Also all 6 windows dont need ot be used. I am really looking for creative design marketing.

The corner 3 windows need the following information: name, expertise, phone number, banner.

Dr. Venn, General Dentistry & Orthodontics, 555.218.7043
Dr. Obradovic, Oral Surgery & Sedation, 555.731.0962

There is also a front door that needs to be designed. The door is 60'' x 36'' (standard door size) We want simple white vinyl on the outside of the door. We need you to organize the information on the door, pick a easy to read font, maybe use the logo and use some of the front window signage aesthetic? Its up to you...but we we were initially thinking of just making the litters white and keep it simple but again you are the designers.

Practice name: Venn and Obradovic General Dentistry & Orthodontics

Address: 4819 Thistle Rd

Phone numbers: Dr. Venn 555.218.7043
Dr. Obradovic 555.731.0962

Hours of operation: Mon: call for an appointment
Tues-Thurs: 9am-5pm
Sat: call for an appointment
Sun: Closed

A line saying we speak Spanish: Se Habla Espanol

*****************************************************************************************************
here are some design that we liked and some rough sketches I made to start the ball rolling. Keep in mind that there are 9 windows for the front because its a corner office, but not all of them have to have stuff on it. We want simple, streamline, classy high commanding price point aesthetic. I am hiring you for your artistic minds.

Target Market(s)

anyone who has dental needs

Industry/Entity Type

Dental

Font styles to use
Serif
Sans Serif

Colors

Designer to choose colors to be used in the design.

Requirements
Must have
• 1. The required information (see project description)
• 2. Logo
• 3. Advertisement banner running along the bottom of all 9 windows (6 in front and 3 on the side)
• NOTE: Look at pictures of the store to get a sense of the customers point of view and also as a reference to how your design will be broken up across several windows or maybe you design something special for every window. But we want the banner to run along all the windows to lead customs to the door on the side. Finally the letters will be done in white vinyl unless state otherwise, remember the window needs to let in natural light so the entire window can not be covered in vinyl.
Nice to have
• artistic flare yet simple and sleep and expensive looking aesthetic. work logo into the design.
Should not have
• The goal is to catch someone eye and give them important information about the practice.
• It should not just be words.
• It should not have to many words
• It must be readable font for cards driving by.

```html
<!DOCTYPE html>
<html lang="en">
<head>
<meta charset="utf-8">
<title>Venn and Obradovic Dental &amp; Orthodontics – Front Door Vinyl</title>
<link rel="stylesheet" href="https://fonts.googleapis.com/css2?family=Open+Sans:wght@400;700&family=Arimo:wght@700&display=swap">
<style>
  :root {
    --page-bg: #ffffff;
    --frame: #3a3a3a;
    --ink: #1e1e1e;
    --brand-blue: #1560a6;
    --band-blue: #0b5fa5;
    --chip-grey: #c9c9c9;
  }
  * { box-sizing: border-box; margin: 0; padding: 0; }
  html, body {
    width: 1200px;
    height: 742px;
    overflow: hidden;
    background: var(--page-bg);
  }
  .canvas {
    position: relative;
    width: 1200px;
    height: 742px;
  }
  .door-panel {
    position: absolute;
    left: 422px;
    top: 45px;
    width: 356px;
    height: 652px;
    border: 1.5px solid var(--frame);
    background: var(--page-bg);
    font-family: "Open Sans", Arial, sans-serif;
    color: var(--ink);
  }
  .brand-mark {
    position: absolute;
    top: 146px;
    left: 167px;
    width: 22px;
    height: 22px;
    border-radius: 50%;
    background: var(--brand-blue);
  }
  .brand-name {
    position: absolute;
    top: 200px;
    width: 100%;
    text-align: center;
    color: var(--brand-blue);
    font-weight: 700;
    font-size: 9.5px;
    letter-spacing: 2.6px;
    line-height: 12px;
    text-transform: uppercase;
  }
  .brand-field {
    position: absolute;
    top: 211px;
    width: 100%;
    text-align: center;
    color: var(--ink);
    font-size: 12.5px;
    line-height: 15px;
    text-transform: uppercase;
  }
  .address {
    position: absolute;
    top: 240px;
    width: 100%;
    text-align: center;
    font-size: 12.5px;
  }
  .phones {
    position: absolute;
    top: 270px;
    left: 79px;
    display: flex;
    gap: 12px;
  }
  .phone-chip {
    background: var(--chip-grey);
    color: var(--brand-blue);
    font-family: "Arimo", Arial, sans-serif;
    font-weight: 700;
    font-size: 12.5px;
    line-height: 14px;
    text-align: center;
    padding: 2px 4px;
  }
  .phone-chip.venn { width: 94px; }
  .phone-chip.obradovic { width: 91px; }
  .hours {
    position: absolute;
    top: 334px;
    width: 100%;
    text-align: center;
    font-size: 12.5px;
    line-height: 16.3px;
    list-style: none;
  }
  .spanish {
    position: absolute;
    top: 414px;
    width: 100%;
    text-align: center;
    font-size: 12.5px;
  }
  .banner-band {
    position: absolute;
    top: 477px;
    left: 38px;
    width: 286px;
    height: 35px;
    background: var(--band-blue);
  }
</style>
</head>
<body>
<div class="canvas">
  <section class="door-panel">
    <span class="brand-mark"></span>
    <p class="brand-name">Venn and Obradovic</p>
    <p class="brand-field">Dental &amp; Orthodontics</p>

    <p class="address">4819 Thistle Rd</p>

    <div class="phones">
      <div class="phone-chip venn">Dr. Venn<br>555.218.7043</div>
      <div class="phone-chip obradovic">Dr. Obradovic<br>555.731.0962</div>
    </div>

    <ul class="hours">
      <li>Mon: call for an appointment</li>
      <li>Tues-Thurs: 9am-5pm</li>
      <li>Sat: call for an appointment</li>
      <li>Sun: Closed</li>
    </ul>

    <p class="spanish">Se Habla Espanol</p>

    <div class="banner-band"></div>
  </section>
</div>
</body>
</html>
```